Need a corporate background Image with our existing logo for Zoom or Microsoft Teams

Hi,

We require a corporate background image with our existing logo use with Zoom or Microsoft Teams.

Our existing logo is at https://www.kestrel-dynamicx.com/images/logo_top.png

Thank you.

```html
<!DOCTYPE html>
<html lang="en">
<head>
<meta charset="UTF-8">
<title>Kestrel Dynamicx – Meeting Background</title>
<link rel="stylesheet" href="https://fonts.googleapis.com/css2?family=Archivo:wght@600&display=swap">
<style>
  :root {
    --page-bg: #f3f3f3;
    --navy-deep: #0c2450;
    --navy: #123a6e;
    --teal-glow: #0f5a86;
    --royal: #1a4fb8;
    --globe-light: #dff3f6;
    --globe-aqua: #6fd6e0;
    --globe-blue: #2f6fd8;
    --white: #ffffff;
  }
  * { margin: 0; padding: 0; box-sizing: border-box; }
  html, body {
    width: 1200px;
    height: 746px;
    overflow: hidden;
    background: var(--page-bg);
  }
  .background-slide {
    position: absolute;
    left: 96px;
    top: 90px;
    width: 1008px;
    height: 566px;
    overflow: hidden;
    background:
      radial-gradient(ellipse 420px 320px at 420px 460px, rgba(15, 90, 134, 0.55), transparent 70%),
      linear-gradient(100deg, var(--navy-deep) 0%, var(--navy) 45%, var(--navy-deep) 100%);
  }
  .light-swoosh {
    position: absolute;
    inset: 0;
    width: 100%;
    height: 100%;
  }
  .brand {
    position: absolute;
    left: 52px;
    top: 56px;
    display: flex;
    align-items: center;
    gap: 22px;
    color: var(--white);
    font-family: "Archivo", Arial, sans-serif;
    font-weight: 600;
  }
  .brand-dot {
    width: 48px;
    height: 48px;
    border-radius: 50%;
    background: var(--white);
  }
  .brand-name {
    display: flex;
    flex-direction: column;
    line-height: 1;
  }
  .brand-name .primary {
    font-size: 40px;
    letter-spacing: -1px;
  }
  .brand-name .secondary {
    margin-top: 6px;
    font-size: 11px;
    letter-spacing: 9.4px;
  }
  .globe-illustration {
    position: absolute;
    left: 632px;
    top: 46px;
    width: 432px;
    height: 432px;
    border-radius: 50%;
    background:
      radial-gradient(circle at 32% 28%, var(--globe-light) 0%, rgba(223, 243, 246, 0.6) 22%, transparent 45%),
      radial-gradient(circle at 70% 60%, var(--globe-aqua) 0%, rgba(111, 214, 224, 0.4) 35%, transparent 60%),
      radial-gradient(circle at 50% 50%, var(--globe-blue) 0%, var(--royal) 75%, var(--navy) 100%);
    box-shadow: 0 0 60px rgba(80, 180, 230, 0.35);
  }
</style>
</head>
<body>
  <main class="background-slide">
    <svg class="light-swoosh" viewBox="0 0 1008 566" preserveAspectRatio="none" aria-hidden="true">
      <path d="M150 0 C 230 200, 340 420, 420 566" stroke="#1e4fb0" stroke-opacity="0.45" stroke-width="26" fill="none"/>
      <path d="M250 0 C 300 180, 360 380, 440 566" stroke="#1e55c0" stroke-opacity="0.35" stroke-width="14" fill="none"/>
      <path d="M0 270 C 120 380, 220 480, 300 566" stroke="#1e4fb0" stroke-opacity="0.35" stroke-width="18" fill="none"/>
      <path d="M40 0 C 90 160, 170 360, 260 566" stroke="#2a64cc" stroke-opacity="0.2" stroke-width="10" fill="none"/>
    </svg>

    <div class="brand">
      <span class="brand-dot" aria-hidden="true"></span>
      <span class="brand-name">
        <span class="primary">KESTREL</span>
        <span class="secondary">DYNAMICX</span>
      </span>
    </div>

    <div class="globe-illustration" role="img" aria-label="Glowing digital globe built from hexagon tiles with dotted world map and connected people icons"></div>
  </main>
</body>
</html>
```